Network Video Recorder Sticker

I need a sticker design for a network video recorder (NVR) metal box. It will be on the front cover and will identify my product. The NVR is to be used on boats and record the fishing activities. My company name is TideOptic HD Systems. I prefer a combination of Blue Water color and gray or any other nice combination. My idea is to have something flat and minimalist like an eye with a lens inside and some kind of lines simulating the waves of the sea. Any other idea is welcome. Dimensions file included on Adobe Ilustrator.

Target Market(s)

Marine and fishing vessels

Industry/Entity Type

Product

Colors
0292cd
0555a3
3176b5

Requirements
Nice to have
• minimalist flat waves like desing with some kind of lens like inside a silluotee of a eye. Please note It will the front cover for a network video Recorder uses in Fishing Boats.

```html
<!DOCTYPE html>
<html lang="en">
<head>
<meta charset="UTF-8">
<title>TideOptic HD Systems – NVR Front Sticker</title>
<link rel="stylesheet" href="https://fonts.googleapis.com/css2?family=Open+Sans:wght@600&family=Arimo:ital,wght@0,700;1,700&display=swap">
<style>
  :root {
    --page-bg: #e9e9e9;
    --sticker-bg: #ffffff;
    --brand-blue: #0555a3;
    --mid-blue: #3176b5;
    --water-blue: #0292cd;
    --label-ink: #1f2f5c;
    --indicator: #1e1e1e;
  }
  html, body {
    margin: 0;
    padding: 0;
    width: 1200px;
    height: 1000px;
    overflow: hidden;
    background: var(--page-bg);
  }
  .canvas {
    position: relative;
    width: 1200px;
    height: 1000px;
  }
  .sticker {
    position: absolute;
    left: 133px;
    top: 353px;
    width: 940px;
    height: 228px;
    background: var(--sticker-bg);
  }
  .brand {
    position: absolute;
    left: 70px;
    top: 118px;
    display: flex;
    align-items: center;
    gap: 18px;
  }
  .brand-dot {
    width: 34px;
    height: 34px;
    border-radius: 50%;
    background: var(--water-blue);
  }
  .brand-name {
    margin: 0;
    font-family: "Open Sans", sans-serif;
    font-weight: 600;
    font-size: 40px;
    line-height: 1;
    color: var(--brand-blue);
    white-space: nowrap;
  }
  .model {
    position: absolute;
    right: 15px;
    top: 14px;
    text-align: right;
  }
  .model-number {
    margin: 0;
    font-family: "Arimo", sans-serif;
    font-style: italic;
    font-weight: 700;
    font-size: 40px;
    line-height: 1;
    color: var(--brand-blue);
  }
  .model-type {
    margin: 4px 0 0;
    font-family: "Arimo", sans-serif;
    font-weight: 700;
    font-size: 15px;
    letter-spacing: 0.4px;
    color: var(--brand-blue);
  }
  .indicators {
    position: absolute;
    left: 728px;
    top: 139px;
    display: flex;
    gap: 14px;
  }
  .indicator {
    display: flex;
    flex-direction: column;
    align-items: center;
    gap: 10px;
    font-family: "Arimo", sans-serif;
    font-weight: 700;
    font-size: 15px;
    color: var(--label-ink);
  }
  .indicator-lamp {
    width: 20px;
    height: 20px;
    border-radius: 50%;
    background: var(--indicator);
  }
</style>
</head>
<body>
  <main class="canvas">
    <section class="sticker" aria-label="NVR front cover sticker">
      <div class="brand">
        <span class="brand-dot" aria-hidden="true"></span>
        <h1 class="brand-name">TideOptic HD Systems</h1>
      </div>

      <div class="model">
        <p class="model-number">NVR-6400</p>
        <p class="model-type">Network Video Recorder</p>
      </div>

      <div class="indicators">
        <div class="indicator">
          <span>Disk</span>
          <span class="indicator-lamp" aria-hidden="true"></span>
        </div>
        <div class="indicator">
          <span>Power</span>
          <span class="indicator-lamp" aria-hidden="true"></span>
        </div>
      </div>
    </section>
  </main>
</body>
</html>
```